Images for my Portfolio

Hi,

I will use this theme

http://themes.corvanelli-studio.com/html/nimbra/light/index.html#work

and need 1 nice big image for each of my projects. So we have 9 images at the end but for mockup 1 image is enough for me to get an idea. The images should show different aspects of the site, so for example:

https://www.hopfenglanz.de/

There we have:
- Slideshow
- Configurator
- Cart etc.

Just have a look around and see whats special. Feel free in image-size and styling-elemets: frames, polaroid, 2D, 3D, mobile devices - do whatever you would do if you were me: a web-designer who wants to explain his last projects to the visitors.

Projects are:

https://www.hopfenglanz.de
http://taldorwinkel.de/
http://movirex.de
http://www.bistro-bruehgeraete-welt.de/
http://www.veltrapress.de/blog/info/klebefolien/
http://km-sprachmittlerin.de/de/
http://trn-appraisal.de/
http://zutrittsring-markt7.de/
http://www.blank-und-flink.de/

This is not advertisement for my clients. I sell websites (!) so the purpose of the images is that my visitor can see what is possible if he hires me.

Thanks a lot

```html
<!DOCTYPE html>
<html lang="de">
<head>
<meta charset="utf-8">
<title>Movirex.de – Entsorgungslizenzen</title>
<link href="https://fonts.googleapis.com/css2?family=Open+Sans:ital,wght@0,400;0,700;1,400;1,700&family=Ubuntu:wght@400;500;700&display=swap" rel="stylesheet">
<style>
  :root {
    --lime-top: #cfe24a;
    --lime-mid: #a9d02f;
    --green-deep: #5f9f10;
    --tab-green: #7fb82a;
    --tab-green-dark: #6aa21b;
    --tab-grey: #c9c9cf;
    --tab-grey-dark: #b3b3bb;
    --ink: #222;
    --ink-soft: #3a3a3a;
    --nav-text: #f6fbd8;
    --white: #fff;
  }
  * { box-sizing: border-box; margin: 0; padding: 0; }
  html, body { width: 1200px; height: 844px; overflow: hidden; }
  body { position: relative; background: var(--white); font-family: "Open Sans", sans-serif; }

  .page-header {
    position: absolute; left: 0; top: 0; width: 1200px; height: 559px;
    background: linear-gradient(180deg, var(--lime-top) 0%, var(--lime-mid) 55%, var(--green-deep) 100%);
  }
  .page-floor {
    position: absolute; left: 0; top: 559px; width: 1200px; height: 285px;
    background: repeating-linear-gradient(135deg, #fff 0 6px, #f6f6f6 6px 7px);
  }

  .brand {
    position: absolute; left: 112px; top: 100px;
    display: flex; align-items: center; gap: 10px;
    font-family: "Ubuntu", sans-serif; font-weight: 700; font-size: 26px; color: #1d1d1d;
  }
  .brand-dot { width: 20px; height: 20px; border-radius: 50%; background: #2f6b1a; }

  .main-nav {
    position: absolute; left: 323px; top: 37px; width: 781px; height: 59px;
    background: rgba(255,255,255,0.12);
    display: flex; align-items: center;
    font-family: "Ubuntu", sans-serif; font-weight: 500; font-size: 19px;
  }
  .main-nav a { color: var(--nav-text); text-decoration: none; padding: 0 11px; line-height: 59px; }
  .main-nav a.is-active { background: #111; color: #fff; padding: 0 11px; }

  .welcome-panel {
    position: absolute; left: 96px; top: 167px; width: 1009px; height: 437px;
    background: var(--white);
    box-shadow: 0 30px 28px -18px rgba(0,0,0,0.35), 0 0 0 1px rgba(255,255,255,0.6);
  }
  .tab {
    position: absolute; top: 0; height: 437px; width: 70px;
    display: flex; flex-direction: column; align-items: center; justify-content: flex-end;
    padding-bottom: 22px;
    font-family: "Ubuntu", sans-serif; font-size: 24px;
  }
  .tab-label { writing-mode: vertical-rl; transform: rotate(180deg); margin-bottom: 30px; white-space: nowrap; }
  .tab-number { font-size: 22px; }
  .tab--active { left: 0; background: linear-gradient(90deg, var(--tab-green), var(--tab-green-dark)); color: #fff; font-weight: 500; }
  .tab--vorteile { left: 869px; background: linear-gradient(90deg, var(--tab-grey), var(--tab-grey-dark)); color: #4a4a52; border-left: 1px solid #aaa; }
  .tab--ablauf { left: 939px; background: linear-gradient(90deg, var(--tab-grey), var(--tab-grey-dark)); color: #4a4a52; border-left: 1px solid #aaa; }

  .hero-photo {
    position: absolute; left: 104px; top: 13px; width: 270px; height: 199px;
    border: 1px solid #999;
    background: linear-gradient(160deg, #6d5a4a 0%, #a48a6c 35%, #3a5f9a 55%, #b13a32 65%, #4c3d33 100%);
  }

  .intro { position: absolute; left: 396px; top: 13px; width: 450px; font-style: italic; color: var(--ink-soft); font-size: 14.5px; line-height: 23px; }
  .intro p { margin-bottom: 14px; }
  .intro .lead { font-weight: 700; color: var(--ink); font-size: 15px; }

  .body-copy { position: absolute; left: 102px; top: 240px; width: 750px; font-style: italic; color: var(--ink-soft); font-size: 14.5px; line-height: 23px; }
  .body-copy p { margin-bottom: 15px; }
  .body-copy .cta { font-weight: 700; color: var(--ink); font-size: 15.5px; margin-bottom: 13px; }
</style>
</head>
<body>
  <div class="page-header"></div>
  <div class="page-floor"></div>

  <div class="brand"><span class="brand-dot"></span>Movirex.de</div>

  <nav class="main-nav">
    <a class="is-active" href="#">Lizenz</a>
    <a href="#">Wie funktioniert’s</a>
    <a href="#">Kontakt</a>
    <a href="#">Fragen &amp; Antworten</a>
    <a href="#">AGB</a>
    <a href="#">Impressum</a>
  </nav>

  <section class="welcome-panel">
    <div class="tab tab--active"><span class="tab-label">Willkommen bei Movirex</span><span class="tab-number">1</span></div>

    <div class="hero-photo" role="img" aria-label="Foto: gestapelte, gebrauchte Kartons und Verpackungsmaterial"></div>

    <div class="intro">
      <p>Herzlich Willkommen bei Movirex!</p>
      <p class="lead">Entsorgungslizenzen für Gewerbetreibende, Versandhändler, Bazaro-Händler und Kleinversender.</p>
      <p>Lizenzieren Sie Verpackungsmaterial, Verkaufsverpackungen und Versandverpackungen im Rahmen der Rücknahmepflicht und Verpackungsverordnung mit Hilfe der Movirex-Entsorgungslizenz rechtssicher in einem Dualen System.</p>
    </div>

    <div class="body-copy">
      <p class="cta">Jetzt Lizenz-Rechner nutzen und sofort kostenlos und unverbindlich Angebot erhalten!</p>
      <p>Informieren Sie sich auf unseren Seiten, lernen Sie Movirex und die Vorteile kennen und<br>erwerben Sie noch heute bequem und einfach Ihre Entsorgungslizenz!</p>
      <p>Und das Beste? Movirex arbeitet ohne Grundgebühren, ohne versteckte Kosten und ohne<br>Verträge! Movirex ist preiswert und unabhängig!</p>
    </div>

    <div class="tab tab--vorteile"><span class="tab-label">Die Movirex Vorteile</span><span class="tab-number">2</span></div>
    <div class="tab tab--ablauf"><span class="tab-label">So funktioniert´s</span><span class="tab-number">3</span></div>
  </section>
</body>
</html>
```